Willowmere Therapy (Endure - Renew - Flourish) - Double Sided Business Card

I would like a 2-sided business card. Front: Matte Black or Navy with Logo & Tagline. Back: Name, Address, Phone Number, Email, & Website (maybe would like to include a small map pin-pointing location); Prefer front to be a gold/silver foil (iridescent); Back prefer white or light colored background with lettering that is easy to read and simple

Target Market(s)

Individuals & Couples (13 y.o. - ALL Adults); High end clientele

Industry/Entity Type

Licensed Professional Counselor (Mental Health)

Contact Information for Business Card

Name: Willowmere Therapy; Tagline: Endure - Renew - Flourish; Address: 3175 W. Calder Ave., Suite 842, Fort Worth, TX 76142; Phone: (214) 738-2956; Website: www.WillowmereTherapy.example

Font styles to use
Serif

Requirements
Must have
• Logo on Front (Large) prefer gold/silver foil on a matte dark color (i.e. black, navy, etc.); Back of Card: All other relevant information

```html
<!DOCTYPE html>
<html lang="en">
<head>
<meta charset="utf-8">
<title>Willowmere Therapy – Business Card</title>
<link rel="stylesheet" href="https://fonts.googleapis.com/css2?family=Cinzel:wght@400;500;600&display=swap">
<style>
  :root {
    --backdrop: #3a3b3d;
    --card-black: #111111;
    --gold: #d9b955;
    --silver: #8a8a8a;
    --silver-light: #b0b0b0;
    --ink-dark: #141414;
  }
  * { box-sizing: border-box; margin: 0; padding: 0; }
  html, body {
    width: 1200px;
    height: 1000px;
    overflow: hidden;
  }
  body {
    background: var(--backdrop);
    font-family: "Cinzel", "Times New Roman", serif;
    position: relative;
  }
  .card {
    position: absolute;
    width: 580px;
    height: 330px;
    background: var(--card-black);
    border-radius: 26px;
    overflow: hidden;
    box-shadow: 0 18px 40px rgba(0,0,0,0.45);
  }

  /* Back side: contact details */
  .card-back { left: 70px; top: 90px; }
  .contact-block {
    position: absolute;
    left: 270px;
    top: 52px;
    width: 270px;
  }
  .business-name {
    color: var(--gold);
    font-size: 20px;
    font-weight: 500;
    letter-spacing: 0.5px;
    white-space: nowrap;
  }
  .rule-gold {
    height: 1px;
    background: var(--gold);
    opacity: 0.7;
    margin: 8px 0 6px;
  }
  .job-title {
    color: var(--silver);
    font-size: 11px;
    letter-spacing: 1px;
  }
  .rule-gold.short { width: 120px; margin: 8px 0 12px; opacity: 0.5; }
  .contact-list { list-style: none; }
  .contact-item {
    display: flex;
    align-items: center;
    gap: 12px;
    color: var(--gold);
    font-size: 11.5px;
    margin-bottom: 13px;
    white-space: nowrap;
  }
  .contact-icon { width: 12px; height: 12px; flex: none; fill: var(--silver-light); }
  .address-band {
    position: absolute;
    left: 0;
    right: 0;
    top: 252px;
    height: 34px;
    background: var(--gold);
    display: flex;
    align-items: center;
    justify-content: center;
    color: var(--ink-dark);
    font-size: 12px;
    font-weight: 500;
    letter-spacing: 0.3px;
  }

  /* Front side: name and tagline */
  .card-front { left: 550px; top: 530px; }
  .front-lockup {
    position: absolute;
    inset: 0;
    display: flex;
    flex-direction: column;
    align-items: center;
    justify-content: center;
  }
  .front-mark {
    width: 70px;
    height: 70px;
    border: 4px solid var(--silver);
    border-radius: 50%;
    margin-bottom: 18px;
  }
  .front-name {
    color: var(--gold);
    font-size: 36px;
    font-weight: 500;
    letter-spacing: 1px;
    white-space: nowrap;
    line-height: 1.1;
  }
  .rule-silver {
    width: 420px;
    height: 3px;
    background: var(--silver);
    margin: 12px 0 10px;
  }
  .tagline {
    color: var(--gold);
    font-size: 19px;
    letter-spacing: 0.5px;
    white-space: nowrap;
  }
</style>
</head>
<body>

  <section class="card card-back" aria-label="Back of business card">
    <div class="contact-block">
      <h1 class="business-name">Willowmere Therapy</h1>
      <div class="rule-gold"></div>
      <p class="job-title">CEO - Founder</p>
      <div class="rule-gold short"></div>
      <ul class="contact-list">
        <li class="contact-item">
          <svg class="contact-icon" viewBox="0 0 24 24" aria-hidden="true"><path d="M6.6 10.8a15.1 15.1 0 0 0 6.6 6.6l2.2-2.2a1 1 0 0 1 1-.25 11.4 11.4 0 0 0 3.6.57 1 1 0 0 1 1 1V20a1 1 0 0 1-1 1A17 17 0 0 1 3 4a1 1 0 0 1 1-1h3.5a1 1 0 0 1 1 1c0 1.25.2 2.45.57 3.57a1 1 0 0 1-.25 1z"/></svg>
          <span>(214) 738-2956</span>
        </li>
        <li class="contact-item">
          <svg class="contact-icon" viewBox="0 0 24 24" aria-hidden="true"><path d="M2 5h20v14H2z M4 7v.5l8 5 8-5V7l-8 5z" fill-rule="evenodd"/></svg>
          <span>hello@willowmeretherapy.example</span>
        </li>
        <li class="contact-item">
          <svg class="contact-icon" viewBox="0 0 24 24" aria-hidden="true"><path d="M12 2a7 7 0 0 0-7 7c0 5.2 7 13 7 13s7-7.8 7-13a7 7 0 0 0-7-7zm0 9.5A2.5 2.5 0 1 1 12 6.5a2.5 2.5 0 0 1 0 5z"/></svg>
          <span>www.WillowmereTherapy.example</span>
        </li>
      </ul>
    </div>
    <div class="address-band">3175 W. Calder Ave., Suite 842, Fort Worth, TX 76142</div>
  </section>

  <section class="card card-front" aria-label="Front of business card">
    <div class="front-lockup">
      <div class="front-mark" aria-hidden="true"></div>
      <h2 class="front-name">Willowmere Therapy</h2>
      <div class="rule-silver"></div>
      <p class="tagline">Endure - Renew - Flourish</p>
    </div>
  </section>

</body>
</html>
```